DL size flyer design for renovations and extensions construction company

We are looking for a flyer design for a construction company specialising in renovations, extensions, and minor building works. The aim is for anyone needing any home construction works to pick up the phone and call us. The flyers will be delivered primarily to letterboxes of homes. We want the flyers to stick out from all the other things people get in the mail by any means possible.

Target Market(s)

The audience we target is residential home owners and are looking to deliver these letters to home letterboxes.

Industry/Entity Type

Residential Construction

Font styles to use
Sans Serif

Colors
000000
ffffff

Requirements
Must have
• 1 - Places for 4 photos with descriptions reading: (1) Bathroom Renovations (4) Kitchen Renovations (3) Home Extensions (4) Outdoor works and landscaping. This may be on the reverse side of the DL flyer.
• 2 - Fonts to be used are (1) Brandon Grotesque (All caps) for main heading, (2) Montserrat SemiBold (All caps) for Headings, (3) Lato for text.
• 3 - Copy of the finished document in PDF and indesign formats.
• 4 - Placeholders for copy (look at the plinvaroq.com website for now)
Nice to have
• A modern looking design.
Should not have
• Not all photos attached are necessarily required. Up to you to use your creativity to decide on the best combination.

```html
<!DOCTYPE html>
<html lang="en">
<head>
<meta charset="utf-8">
<title>Plinvaroq Homes – DL Flyer</title>
<link href="https://fonts.googleapis.com/css2?family=Montserrat:wght@500;600;700;800&family=Lato:wght@400;700&display=swap" rel="stylesheet">
<style>
  :root {
    --green: #0e9a56;
    --green-bright: #12aa5e;
    --green-dark: #0a7f46;
    --black: #111111;
    --white: #ffffff;
    --row-grey: #f1f2f2;
    --stage: #a3a3a3;
    --text: #1d1d1d;
  }
  * { box-sizing: border-box; margin: 0; padding: 0; }
  html, body { width: 1200px; height: 943px; overflow: hidden; }
  body { background: var(--stage); position: relative; font-family: "Lato", sans-serif; color: var(--text); }

  .flyer { position: absolute; top: 52px; width: 424px; height: 849px; background: var(--white); overflow: hidden; }
  .flyer--front { left: 106px; }
  .flyer--back { left: 664px; }

  .brand { position: absolute; left: 0; right: 0; text-align: center; font-family: "Montserrat", sans-serif; font-weight: 800; color: var(--black); letter-spacing: 0.5px; }
  .flyer--front .brand { top: 52px; font-size: 34px; }
  .flyer--back .brand { top: 28px; font-size: 24px; }

  .hero { position: absolute; left: 0; top: 106px; width: 424px; height: 470px; }

  .headline { position: absolute; top: 610px; left: 0; right: 0; text-align: center; font-family: "Montserrat", sans-serif; font-weight: 700; font-size: 27px; line-height: 33px; text-transform: uppercase; color: var(--black); }
  .headline .accent { color: var(--green); }

  .services { position: absolute; top: 700px; left: 22px; right: 22px; display: flex; justify-content: space-between; }
  .service { width: 110px; text-align: center; font-family: "Montserrat", sans-serif; font-weight: 600; font-size: 16px; color: var(--black); }
  .service svg { display: block; margin: 0 auto 12px; }

  .web { position: absolute; left: 0; right: 0; text-align: center; font-family: "Montserrat", sans-serif; font-weight: 600; font-size: 16px; color: var(--black); display: flex; justify-content: center; align-items: center; gap: 8px; }
  .web::before, .web::after { content: ""; width: 66px; height: 2px; background: var(--green); }
  .web b { color: var(--green); font-weight: 700; }
  .flyer--front .web { top: 808px; }
  .flyer--back .web { top: 810px; }

  .offer { position: absolute; left: 0; width: 424px; display: flex; align-items: center; gap: 18px; padding: 0 26px; }
  .offer--shaded { background: var(--row-grey); }
  .offer--reverse { flex-direction: row-reverse; }
  .offer__photo { flex: none; width: 141px; height: 94px; border: 3px solid #c9c9c9; outline: 1px solid #ffffff; outline-offset: -5px; }
  .offer__title { font-family: "Montserrat", sans-serif; font-weight: 700; font-size: 15px; color: var(--green); text-transform: uppercase; margin-bottom: 6px; line-height: 19px; }
  .offer__text { font-size: 12.3px; line-height: 15px; color: var(--text); }

  .backdrop { position: absolute; left: 0; top: 620px; width: 424px; height: 229px; }

  .quote { position: absolute; top: 686px; left: 0; right: 0; text-align: center; }
  .quote__label { font-family: "Montserrat", sans-serif; font-weight: 700; font-size: 24px; color: var(--black); }
  .quote__label span { background: var(--green); color: var(--white); padding: 0 4px; border-radius: 3px; }
  .quote__phone { font-family: "Montserrat", sans-serif; font-weight: 700; font-size: 35px; color: var(--black); margin-top: 2px; letter-spacing: 0.5px; }

  .contact { position: absolute; top: 772px; left: 0; right: 0; display: flex; justify-content: center; align-items: center; gap: 10px; font-size: 13px; color: var(--text); }
  .contact__item { display: flex; align-items: center; gap: 7px; }
  .contact__divider { width: 2px; height: 22px; background: var(--green); }
</style>
</head>
<body>

<section class="flyer flyer--front">
  <div class="brand">PLINVAROQ HOMES</div>

  <svg class="hero" viewBox="0 0 424 470" aria-hidden="false">
    <defs>
      <linearGradient id="heroTone" x1="0" y1="0" x2="0" y2="1">
        <stop offset="0" stop-color="#ece8e3"/>
        <stop offset="0.5" stop-color="#b89e86"/>
        <stop offset="1" stop-color="#d8cfc4"/>
      </linearGradient>
    </defs>
    <path role="img" aria-label="Photo of a smiling family lying together on a living room rug" d="M0 0 H424 V385 C330 470 130 470 0 345 Z" fill="url(#heroTone)"/>
    <path d="M0 345 C130 470 330 470 424 385 V410 C330 500 110 500 0 372 Z" fill="var(--green-bright)"/>
    <path d="M0 380 C110 510 330 510 424 420 V432 C330 530 100 530 0 400 Z" fill="var(--green-dark)"/>
  </svg>

  <h1 class="headline">Looking to make your<br><span class="accent">Home bigger or better?</span></h1>

  <div class="services">
    <div class="service">
      <svg width="48" height="48" viewBox="0 0 48 48"><circle cx="24" cy="24" r="24" fill="var(--green)"/><g stroke="#fff" stroke-width="3.5" stroke-linecap="round"><line x1="14" y1="34" x2="32" y2="16"/><line x1="16" y1="16" x2="34" y2="34"/></g><rect x="11" y="11" width="10" height="6" rx="1" fill="#fff" transform="rotate(45 16 14)"/><circle cx="33" cy="15" r="4" fill="none" stroke="#fff" stroke-width="3"/></svg>
      BUILD
    </div>
    <div class="service">
      <svg width="48" height="48" viewBox="0 0 48 48"><circle cx="24" cy="24" r="24" fill="var(--green)"/><circle cx="24" cy="24" r="15" fill="none" stroke="#fff" stroke-width="2.5" stroke-dasharray="20 4"/><rect x="18" y="15" width="12" height="18" fill="#fff"/><g fill="var(--green)"><rect x="20" y="17" width="3" height="3"/><rect x="25" y="17" width="3" height="3"/><rect x="20" y="22" width="3" height="3"/><rect x="25" y="22" width="3" height="3"/><rect x="20" y="27" width="3" height="3"/><rect x="25" y="27" width="3" height="3"/></g></svg>
      RENOVATE
    </div>
    <div class="service">
      <svg width="48" height="48" viewBox="0 0 48 48"><circle cx="24" cy="24" r="24" fill="var(--green)"/><g stroke="#fff" stroke-width="2.8" fill="none" stroke-linecap="round"><path d="M13 19 V13 H19 M13 13 L20 20"/><path d="M35 19 V13 H29 M35 13 L28 20"/><path d="M13 29 V35 H19 M13 35 L20 28"/><path d="M35 29 V35 H29 M35 35 L28 28"/></g></svg>
      EXTEND
    </div>
  </div>

  <div class="web">www.<b>plinvaroq</b>.com</div>
</section>

<section class="flyer flyer--back">
  <div class="brand">PLINVAROQ HOMES</div>

  <article class="offer" style="top:76px;height:110px;">
    <div class="offer__photo" role="img" aria-label="Photo of a bright renovated bathroom with glass shower" style="background:linear-gradient(135deg,#e8e8e6,#a9a6a1)"></div>
    <div>
      <h2 class="offer__title">Bathroom Renovations</h2>
      <p class="offer__text">We create custom bathroom renovations of various shapes and sizes to suit a variety of family needs.</p>
    </div>
  </article>

  <article class="offer offer--shaded offer--reverse" style="top:186px;height:120px;">
    <div class="offer__photo" role="img" aria-label="Photo of a modern open-plan kitchen" style="background:linear-gradient(135deg,#f2f1ee,#b9b2a8)"></div>
    <div>
      <h2 class="offer__title">Kitchen Renovations</h2>
      <p class="offer__text">Today's kitchens go further than places to just make a meal - they are the open-plan hub for the modern home.</p>
    </div>
  </article>

  <article class="offer" style="top:306px;height:126px;">
    <div class="offer__photo" role="img" aria-label="Photo of an extended dining and living area" style="background:linear-gradient(135deg,#e6e2dc,#9a6f4a)"></div>
    <div>
      <h2 class="offer__title">Home Extensions</h2>
      <p class="offer__text">PlinvaroqHomes are licenced builders experienced at delivering structural alterations or home extensions, and we are always guided by our qualified engineers.</p>
    </div>
  </article>

  <article class="offer offer--shaded offer--reverse" style="top:432px;height:120px;">
    <div class="offer__photo" role="img" aria-label="Photo of a renovated interior with glass shower" style="background:linear-gradient(135deg,#e4e3e0,#8f8b86)"></div>
    <div>
      <h2 class="offer__title">Outdoor works and landscaping</h2>
      <p class="offer__text">Home living spans across both internal and external environments and a complete home needs to consider integration into the surrounding land.</p>
    </div>
  </article>

  <svg class="backdrop" viewBox="0 0 424 229" preserveAspectRatio="none" aria-hidden="true">
    <defs>
      <radialGradient id="softGrey" cx="0.5" cy="0.6" r="0.7">
        <stop offset="0" stop-color="#ffffff"/>
        <stop offset="1" stop-color="#e9eaea"/>
      </radialGradient>
    </defs>
    <path d="M0 165 C70 50 250 -10 424 80 V229 H0 Z" fill="url(#softGrey)"/>
    <path d="M0 150 C80 30 250 -20 424 62 V88 C260 5 90 50 0 178 Z" fill="var(--green-bright)"/>
    <path d="M30 170 C120 70 260 40 424 100 V106 C270 55 130 85 30 176 Z" fill="var(--green-dark)"/>
  </svg>

  <div class="quote">
    <div class="quote__label">REQUEST <span>A QUOTE</span></div>
    <div class="quote__phone">0412 555 019</div>
  </div>

  <div class="contact">
    <span class="contact__item"><svg width="11" height="9" viewBox="0 0 11 9"><rect width="11" height="9" fill="var(--green)"/><path d="M0 0 L5.5 5 L11 0" stroke="#fff" fill="none"/></svg>info@plinvaroq.com</span>
    <span class="contact__divider"></span>
    <span class="contact__item"><svg width="10" height="13" viewBox="0 0 10 13"><path d="M5 13 C2 9 0 7 0 5 A5 5 0 0 1 10 5 C10 7 8 9 5 13 Z" fill="var(--green)"/><circle cx="5" cy="5" r="2" fill="#fff"/></svg>Sydney, NSW.</span>
  </div>

  <div class="web">www.<b>plinvaroq</b>.com</div>
</section>

</body>
</html>
```